Paloverde Coffee and Kitchen needs a food menu.

We need a menu design for a small coffeeshop in San Pedro Sula Honduras. We serve bistro style food. It should look clean, eye pleasing, modern and organic.
We are all about the home made feel. Superb quality, only natural ingredients, everything is made from scratch. We serve soups, sandwiches, salads, we specialize in desserts and gelato. We are located inside a hotel, we have both english and spanish speaking customers.

Target Market(s)

Young adults

Industry/Entity Type

Restaurant

Contact Information for Business Card

Paloverde
info@paloverdemx.example
Hotel Brisa Lodge Plaza, San Pedro Sula Honduras
+50427408263

Font styles to use
Sans Serif

Colors

Designer to choose colors to be used in the design.

Requirements
Must have
• elegant and clean feel.
Nice to have
• lettering.

```html
<!DOCTYPE html>
<html lang="es">
<head>
<meta charset="utf-8">
<title>Paloverde Coffee and Kitchen — Menú</title>
<link rel="stylesheet" href="https://fonts.googleapis.com/css2?family=Mulish:ital,wght@0,400;0,600;0,800;0,900;1,400;1,700&display=swap">
<style>
  :root{
    --red:#d3222a;
    --ink:#1c1c1c;
    --paper:#ffffff;
    --backdrop:#dcdcdc;
  }
  *{box-sizing:border-box;margin:0;padding:0}
  html,body{width:1200px;height:849px;overflow:hidden}
  body{background:var(--backdrop);font-family:'Mulish',sans-serif;color:var(--ink);position:relative}

  .sheet{position:absolute;top:223px;width:675px;height:477px;background:var(--paper);
    transform:scale(.844);transform-origin:top left;overflow:hidden}
  .sheet--front{left:20px}
  .sheet--back{left:610px}
  .sheet > *{position:absolute}

  /* brand */
  .brand{left:0;width:675px;top:30px;text-align:center;font-weight:800;font-size:44px;letter-spacing:-1px;color:var(--ink);line-height:1}
  .brand-dot{display:inline-block;width:14px;height:14px;border-radius:50%;background:var(--ink);margin-left:6px;vertical-align:middle}
  .tagline{left:0;width:675px;text-align:center;font-style:italic;font-weight:700;line-height:1}
  .tagline--es{top:98px;font-size:10px;color:var(--red)}
  .tagline--en{top:109px;font-size:7px;color:var(--ink)}
  .rule{left:10px;width:655px;top:125px;border-top:1.3px dotted var(--red)}

  /* sections */
  .frame{border:1.3px dotted var(--red);border-radius:10px}
  .section-title{color:var(--red);font-weight:800;font-size:16px;line-height:1;background:var(--paper);padding-right:4px;text-transform:uppercase}
  .section-sub{font-style:italic;font-weight:700;font-size:5.5px;line-height:1}
  .dash{border-top:1.3px dotted var(--red)}

  /* menu items */
  .item{line-height:1.15}
  .item-name{font-weight:800;font-size:7.5px;text-transform:uppercase;display:flex;justify-content:space-between}
  .item-price{font-weight:600}
  .item-sub{font-style:italic;font-size:5.5px;font-weight:600;text-transform:uppercase;margin-bottom:3px}
  .item-sub.lower{text-transform:none}
  .item-note{font-size:5.5px}
  .item-note.en{font-style:italic}
  .drink{display:flex;justify-content:space-between;font-size:7px;font-weight:800;text-transform:uppercase;line-height:1}

  .photo-band{left:0;top:0;width:675px;height:477px;pointer-events:none}
  .mini-brand{font-weight:800;font-size:9px;line-height:1;color:var(--ink)}
  .mini-brand .brand-dot{width:5px;height:5px;margin-left:2px}
</style>
</head>
<body>

<!-- FRONT -->
<section class="sheet sheet--front">
  <div class="brand">paloverde<span class="brand-dot"></span></div>
  <p class="tagline tagline--es">sensación casera, excelente calidad y solo ingredientes naturales</p>
  <p class="tagline tagline--en">home made feel, superb quality, and only natural ingredients</p>
  <div class="rule"></div>

  <div class="frame" style="left:12px;top:135px;width:150px;height:280px"></div>
  <div class="frame" style="left:328px;top:135px;width:154px;height:180px"></div>

  <h2 class="section-title" style="left:21px;top:138px">Appetizers</h2>
  <p class="section-sub" style="left:21px;top:156px">appetizers</p>
  <h2 class="section-title" style="left:180px;top:138px">Sopas</h2>
  <p class="section-sub" style="left:180px;top:156px">soups</p>
  <h2 class="section-title" style="left:339px;top:138px">Salads</h2>
  <p class="section-sub" style="left:339px;top:156px">salads</p>
  <h2 class="section-title" style="left:497px;top:138px">Sandwiches</h2>
  <p class="section-sub" style="left:497px;top:156px">sandwich</p>

  <!-- appetizers -->
  <div class="item" style="left:21px;top:181px;width:131px"><p class="item-name">Patatas Bravas<span class="item-price">9.9</span></p><p class="item-sub">Spicy potatoes</p><p class="item-note">explanation of ingredient in Spanish</p><p class="item-note en">explanation of ingredient in English</p></div>
  <div class="item" style="left:21px;top:228px;width:131px"><p class="item-name">Patatas Bravas<span class="item-price">9.9</span></p><p class="item-sub">Spicy potatoes</p><p class="item-note">explanation of ingredient in Spanish</p><p class="item-note en">explanation of ingredient in English</p></div>
  <div class="item" style="left:21px;top:275px;width:131px"><p class="item-name">Patatas Bravas<span class="item-price">9.9</span></p><p class="item-sub">Spicy potatoes</p><p class="item-note">explanation of ingredient in Spanish</p><p class="item-note en">explanation of ingredient in English</p></div>
  <div class="item" style="left:21px;top:322px;width:131px"><p class="item-name">Patatas Bravas<span class="item-price">9.9</span></p><p class="item-sub">Spicy potatoes</p><p class="item-note">explanation of ingredient in Spanish</p><p class="item-note en">explanation of ingredient in English</p></div>
  <div class="item" style="left:21px;top:369px;width:131px"><p class="item-name">Patatas Bravas<span class="item-price">9.9</span></p><p class="item-sub">Spicy potatoes</p><p class="item-note">explanation of ingredient in Spanish</p><p class="item-note en">explanation of ingredient in English</p></div>

  <!-- soups -->
  <div class="item" style="left:180px;top:181px;width:130px"><p class="item-name">Sopas to dos los Diaz<span class="item-price">9.9</span></p><p class="item-sub">Diaz soup</p><p class="item-note">explanation of ingredient in Spanish</p><p class="item-note en">explanation of ingredient in English</p></div>
  <div class="item" style="left:180px;top:228px;width:130px"><p class="item-name">Sopa e Caracol<span class="item-price">9.9</span></p><p class="item-sub">Caracol soup</p><p class="item-note">explanation of ingredient in Spanish</p><p class="item-note en">explanation of ingredient in English</p></div>
  <div class="item" style="left:180px;top:275px;width:130px"><p class="item-name">Sopa e Caracol<span class="item-price">9.9</span></p><p class="item-sub">Caracol soup</p><p class="item-note">explanation of ingredient in Spanish</p><p class="item-note en">explanation of ingredient in English</p></div>
  <div class="item" style="left:180px;top:322px;width:130px"><p class="item-name">Sopa e Caracol<span class="item-price">9.9</span></p><p class="item-sub">Caracol soup</p><p class="item-note">explanation of ingredient in Spanish</p><p class="item-note en">explanation of ingredient in English</p></div>

  <!-- salads -->
  <div class="item" style="left:339px;top:181px;width:131px"><p class="item-name">Ensalada de Salmón<span class="item-price">9.9</span></p><p class="item-sub">Salmon salad</p><p class="item-note">explanation of ingredient in Spanish</p><p class="item-note en">explanation of ingredient in English</p></div>
  <div class="item" style="left:339px;top:228px;width:131px"><p class="item-name">Ensalada de Salmón<span class="item-price">9.9</span></p><p class="item-sub">Salmon salad</p><p class="item-note">explanation of ingredient in Spanish</p><p class="item-note en">explanation of ingredient in English</p></div>
  <div class="item" style="left:339px;top:275px;width:131px"><p class="item-name">Ensalada de Salmón<span class="item-price">9.9</span></p><p class="item-sub">Salmon salad</p><p class="item-note">explanation of ingredient in Spanish</p><p class="item-note en">explanation of ingredient in English</p></div>

  <!-- sandwiches -->
  <div class="item" style="left:497px;top:181px;width:134px"><p class="item-name">Sandwich Cubano<span class="item-price">9.9</span></p><p class="item-sub">Cubano sandwich</p><p class="item-note">explanation of ingredient in Spanish</p><p class="item-note en">explanation of ingredient in English</p></div>
  <div class="item" style="left:497px;top:228px;width:134px"><p class="item-name">Sandwich Cubano<span class="item-price">9.9</span></p><p class="item-sub">Cubano sandwich</p><p class="item-note">explanation of ingredient in Spanish</p><p class="item-note en">explanation of ingredient in English</p></div>
  <div class="item" style="left:497px;top:275px;width:134px"><p class="item-name">Sandwich Cubano<span class="item-price">9.9</span></p><p class="item-sub">Cubano sandwich</p></div>

  <svg class="photo-band" viewBox="0 0 675 477" aria-hidden="false">
    <defs>
      <linearGradient id="gNuts" x1="0" y1="0" x2="1" y2="1"><stop offset="0" stop-color="#a78a68"/><stop offset="1" stop-color="#5c4430"/></linearGradient>
      <linearGradient id="gShrimp" x1="0" y1="0" x2="1" y2="1"><stop offset="0" stop-color="#c8b9a6"/><stop offset="1" stop-color="#7a5537"/></linearGradient>
      <linearGradient id="gStew" x1="0" y1="0" x2="1" y2="1"><stop offset="0" stop-color="#e6b04a"/><stop offset="1" stop-color="#c0453a"/></linearGradient>
      <linearGradient id="gSalad" x1="0" y1="0" x2="1" y2="1"><stop offset="0" stop-color="#c9d3a8"/><stop offset="1" stop-color="#5e7a36"/></linearGradient>
      <linearGradient id="gSandwich" x1="0" y1="0" x2="1" y2="1"><stop offset="0" stop-color="#d7b48a"/><stop offset="1" stop-color="#8a5a2e"/></linearGradient>
    </defs>
    <polygon role="img" aria-label="Photo of roasted nuts appetizer" fill="url(#gNuts)" points="0,460 150,422 150,477 0,477"/>
    <polygon role="img" aria-label="Photo of grilled shrimp dish" fill="url(#gShrimp)" points="155,420 305,382 305,477 155,477"/>
    <polygon role="img" aria-label="Photo of vegetable stew in a red bowl" fill="url(#gStew)" points="312,380 437,349 437,477 312,477"/>
    <polygon role="img" aria-label="Photo of salmon salad with egg" fill="url(#gSalad)" points="445,347 560,317 560,477 445,477"/>
    <polygon role="img" aria-label="Photo of Cuban sandwich with fries" fill="url(#gSandwich)" points="567,315 675,288 675,477 567,477"/>
  </svg>
</section>

<!-- BACK -->
<section class="sheet sheet--back">
  <!-- desserts -->
  <h2 class="section-title" style="left:19px;top:23px">Paloverde</h2>
  <p class="section-sub" style="left:19px;top:41px">desserts</p>
  <div class="item" style="left:19px;top:68px;width:134px"><p class="item-name">Yougurt Brulle<span class="item-price">9.9</span></p><p class="item-sub lower">yougurt brulle</p><p class="item-note">explanation of ingredient in Spanish</p><p class="item-note en">explanation of ingredient in English</p></div>
  <div class="item" style="left:19px;top:115px;width:134px"><p class="item-name">Yougurt Brulle<span class="item-price">9.9</span></p><p class="item-sub lower">yougurt brulle</p><p class="item-note">explanation of ingredient in Spanish</p><p class="item-note en">explanation of ingredient in English</p></div>
  <div class="item" style="left:19px;top:162px;width:134px"><p class="item-name">Yougurt Brulle<span class="item-price">9.9</span></p><p class="item-sub lower">yougurt brulle</p><p class="item-note">explanation of ingredient in Spanish</p><p class="item-note en">explanation of ingredient in English</p></div>

  <!-- wine -->
  <div class="frame" style="left:167px;top:30px;width:295px;height:112px"></div>
  <h2 class="section-title" style="left:175px;top:21px;padding-left:2px">Wine &amp; Liqueurs</h2>
  <p class="section-sub" style="left:177px;top:39px">wine &amp; liquors</p>
  <div style="left:179px;top:67px;width:110px;display:grid;row-gap:11px">
    <p class="drink">Red Wine<span>9.9</span></p><p class="drink">White Wine<span>9.9</span></p><p class="drink">Martini<span>9.9</span></p><p class="drink">Mojito<span>9.9</span></p>
  </div>
  <div style="left:337px;top:67px;width:110px;display:grid;row-gap:11px">
    <p class="drink">Beer<span>9.9</span></p><p class="drink">White Wine<span>9.9</span></p><p class="drink">Martini<span>9.9</span></p><p class="drink">Mojito<span>9.9</span></p>
  </div>

  <!-- coffee -->
  <div class="frame" style="left:489px;top:30px;width:148px;height:140px"></div>
  <h2 class="section-title" style="left:497px;top:21px;padding-left:2px">Café &amp; Té</h2>
  <p class="section-sub" style="left:499px;top:39px">coffee</p>
  <div style="left:499px;top:68px;width:90px;display:grid;row-gap:9.5px">
    <p class="drink">Espresso<span>9.9</span></p><p class="drink">Espresso<span>9.9</span></p><p class="drink">Espresso<span>9.9</span></p><p class="drink">Espresso<span>9.9</span></p><p class="drink">Espresso<span>9.9</span></p><p class="drink">Matcha<span>9.9</span></p>
  </div>

  <svg class="photo-band" viewBox="0 0 675 477">
    <defs>
      <clipPath id="diamond"><polygon points="0,245 349,162 675,245 349,328"/></clipPath>
      <linearGradient id="gCream" x1="0" y1="0" x2="0" y2="1"><stop offset="0" stop-color="#ece6d4"/><stop offset="1" stop-color="#c9b98f"/></linearGradient>
      <linearGradient id="gGelato" x1="0" y1="0" x2="0" y2="1"><stop offset="0" stop-color="#f1d77e"/><stop offset="1" stop-color="#b9913f"/></linearGradient>
      <linearGradient id="gMeringue" x1="0" y1="0" x2="0" y2="1"><stop offset="0" stop-color="#f4f0ea"/><stop offset="1" stop-color="#cfc5b7"/></linearGradient>
      <linearGradient id="gCookie" x1="0" y1="0" x2="0" y2="1"><stop offset="0" stop-color="#d9d5cc"/><stop offset="1" stop-color="#3a3835"/></linearGradient>
      <linearGradient id="gWine" x1="0" y1="0" x2="0" y2="1"><stop offset="0" stop-color="#8a6b5a"/><stop offset="1" stop-color="#4a1a1e"/></linearGradient>
      <linearGradient id="gBeer" x1="0" y1="0" x2="0" y2="1"><stop offset="0" stop-color="#6f8fa8"/><stop offset="1" stop-color="#b98a3c"/></linearGradient>
      <linearGradient id="gLatte" x1="0" y1="0" x2="0" y2="1"><stop offset="0" stop-color="#e9e4dc"/><stop offset="1" stop-color="#a0754c"/></linearGradient>
      <linearGradient id="gBurger" x1="0" y1="0" x2="0" y2="1"><stop offset="0" stop-color="#c9a577"/><stop offset="1" stop-color="#6a4a2c"/></linearGradient>
    </defs>
    <g clip-path="url(#diamond)">
      <rect role="img" aria-label="Photo of yogurt brûlée dessert" x="2" y="150" width="85" height="190" fill="url(#gCream)"/>
      <rect role="img" aria-label="Photo of mango gelato in a glass" x="96" y="150" width="78" height="190" fill="url(#gGelato)"/>
      <rect role="img" aria-label="Photo of white meringues" x="185" y="150" width="72" height="190" fill="url(#gMeringue)"/>
      <rect role="img" aria-label="Photo of cookies and cream gelato" x="268" y="150" width="66" height="190" fill="url(#gCookie)"/>
      <rect role="img" aria-label="Photo of red wine bottles and glass" x="343" y="150" width="66" height="190" fill="url(#gWine)"/>
      <rect role="img" aria-label="Photo of beer bottles at the bar" x="419" y="150" width="72" height="190" fill="url(#gBeer)"/>
      <rect role="img" aria-label="Photo of a latte with foam art" x="501" y="150" width="80" height="190" fill="url(#gLatte)"/>
      <rect role="img" aria-label="Photo of a hamburger" x="591" y="150" width="84" height="190" fill="url(#gBurger)"/>
    </g>
    <polygon points="0,245 349,162 675,245 349,328" fill="none" stroke="#d3222a" stroke-width="1.3" stroke-dasharray="1.5 2.5"/>
  </svg>

  <!-- gelato -->
  <div class="frame" style="left:12px;top:340px;width:312px;height:125px"></div>
  <h2 class="section-title" style="left:15px;top:329px;padding-left:4px">Gelato &amp; Sorbets</h2>
  <p class="section-sub" style="left:19px;top:347px">gelato &amp; sorbets</p>
  <div class="item" style="left:20px;top:372px;width:134px"><p class="item-name">Gelato Vegano<span class="item-price">9.9</span></p><p class="item-sub lower">gelato vegano</p><p class="item-note">explanation of ingredient in Spanish</p><p class="item-note en">explanation of ingredient in English</p></div>
  <div class="item" style="left:20px;top:419px;width:134px"><p class="item-name">Gelato Vegano<span class="item-price">9.9</span></p><p class="item-sub lower">gelato vegano</p><p class="item-note">explanation of ingredient in Spanish</p><p class="item-note en">explanation of ingredient in English</p></div>
  <div class="item" style="left:179px;top:372px;width:134px"><p class="item-name">Gelato Vegano<span class="item-price">9.9</span></p><p class="item-sub lower">gelato vegano</p><p class="item-note">explanation of ingredient in Spanish</p><p class="item-note en">explanation of ingredient in English</p></div>
  <div class="item" style="left:179px;top:419px;width:134px"><p class="item-name">Gelato Vegano<span class="item-price">9.9</span></p><p class="item-sub lower">gelato vegano</p><p class="item-note">explanation of ingredient in Spanish</p><p class="item-note en">explanation of ingredient in English</p></div>

  <!-- other -->
  <h2 class="section-title" style="left:337px;top:340px">Otro</h2>
  <p class="section-sub" style="left:337px;top:358px">other</p>
  <div class="item" style="left:337px;top:375px;width:134px"><p class="item-name">Hamburguesa<span class="item-price">9.9</span></p><p class="item-sub lower">burger</p><p class="item-note">explanation of ingredient in Spanish</p><p class="item-note en">explanation of ingredient in English</p></div>
  <div class="item" style="left:337px;top:421px;width:134px"><p class="item-name">Hamburguesa<span class="item-price">9.9</span></p><p class="item-sub lower">burger</p><p class="item-note">explanation of ingredient in Spanish</p><p class="item-note en">explanation of ingredient in English</p></div>

  <div class="item" style="left:499px;top:317px;width:132px"><p class="item-name">Hamburguesa<span class="item-price">9.9</span></p><p class="item-sub lower">burger</p><p class="item-note">explanation of ingredient in Spanish</p><p class="item-note en">explanation of ingredient in English</p></div>
  <div class="item" style="left:499px;top:363px;width:132px"><p class="item-name">Hamburguesa<span class="item-price">9.9</span></p><p class="item-sub lower">burger</p><p class="item-note">explanation of ingredient in Spanish</p><p class="item-note en">explanation of ingredient in English</p></div>
  <div class="item" style="left:499px;top:409px;width:132px"><p class="item-name">Hamburguesa<span class="item-price">9.9</span></p><p class="item-sub lower">burger</p><p class="item-note">explanation of ingredient in Spanish</p><p class="item-note en">explanation of ingredient in English</p></div>

  <p class="mini-brand" style="left:604px;top:442px">paloverde<span class="brand-dot"></span></p>
</section>

</body>
</html>
```